Visual design for database driven web application

Need a clean, professional looking visual design for a web application.

PLUME is the new standardized K-12 school testing program for the state of Texas. We are building an application named PLUME-Finder (clever, yeah?) that will allow teachers, school administrators, and others to EASILY sort through millions of records of student data and print or export reports showing just the information they need about their students.

The state currently doesn't provide a user-friendly way to do this. They provide a "data dump" spreadsheet that school administrators and teachers must figure out how to manipulate to get the data they need. We are building a Web-based tool that will make it super simple and easy for our users to get the data they need in a format that works for them.

I've created a basic wireframe of the main application screen in Vellum QD Max. I need you to "skin" the wireframe to make it look good. Your mockup will set the tone for branding and visual design throughout the site.

See the attached screenshots. There are a few variations of the screen that include dynamic panels that open & close. Start by designing just the main screen and if you have time, do one or two of the panels. Thanks!
Updates

Target Market(s)

K-12 education professionals (teachers, administrators) in the state of Texas

Industry/Entity Type

Building

Requirements
Must have
• Your mockups should include all of the features & content shown in the attached screenshots.

However, you don't have to show all 10 rows of data. You can just do the column headers and one row of data. (It would be repetitive and unnecessary to spend time re-creating the entire grid with all of that data just to show your visual styling.)

The design should reflect the following concepts:

- Texas
- Education
- Simplicity
- Helpfulness
- Trust
- Professionalism

If I select your design, I will want your design source files (Illustrator, Photoshop, etc.)
Nice to have
• A logo in the upper left corner for PLUME-Finder. The logo should definitely communicate the design concepts described under "must have."

```html
<!DOCTYPE html>
<html lang="en">
<head>
<meta charset="utf-8">
<title>PLUME-Finder — Student Data</title>
<link rel="stylesheet" href="https://fonts.googleapis.com/css2?family=Arimo:wght@400;700&display=swap">
<style>
:root{
  --navy:#17386b;
  --orange:#e8891c;
  --ink:#333;
  --link-red:#a31515;
  --blue:#4a90d4;
  --blue-light:#66aae2;
  --nav-dark:#262c33;
  --nav-mid:#3a4149;
  --rule:#d6d6d6;
  --bar:#f4f4f4;
  --green:#2f8f2f;
}
*{box-sizing:border-box;margin:0;padding:0}
html,body{width:1200px;height:609px;overflow:hidden}
body{font-family:"Arimo",Arial,sans-serif;color:var(--ink);background:#fff;position:relative}
.abs{position:absolute;white-space:nowrap}

/* header */
.site-header{position:absolute;left:0;top:0;width:1200px;height:90px;background:linear-gradient(#f7f7f7,#e4e4e4)}
.brand{left:18px;top:8px;width:120px;height:76px}
.brand-mark{position:absolute;left:38px;top:4px;width:40px;height:40px;border-radius:50%;background:var(--blue-light)}
.brand-name{position:absolute;left:2px;top:56px;font-weight:700;font-size:17px;color:var(--navy);white-space:nowrap}
.welcome{left:517px;top:33px;font-size:20px;font-weight:700;color:var(--navy)}
.welcome .user{color:var(--orange);margin-left:6px}
.account{left:684px;top:39px;font-size:14px;color:var(--navy)}
.account-icon{top:19px}
.search-field{left:899px;top:25px;width:194px;height:23px;border:1px solid #cfcfcf;border-radius:4px;background:#fff}
.search-button{left:1097px;top:25px;width:92px;height:23px;border-radius:4px;background:linear-gradient(#7db8e6,#4a90d4);color:#fff;font-size:13px;text-align:center;line-height:23px}
.search-options{right:30px;top:64px;font-size:12px;color:var(--navy);text-decoration:underline}

/* nav */
.main-nav{position:absolute;left:0;top:90px;width:1200px;height:40px;background:linear-gradient(var(--nav-mid),var(--nav-dark))}
.nav-tab{position:absolute;top:0;height:40px;line-height:42px;color:#fff;font-size:15px;text-align:center}
.nav-tab.active{background:linear-gradient(#75b3e5,#4f95d2)}
.nav-rule{position:absolute;left:0;top:130px;width:1200px;height:7px;background:var(--blue)}

/* toolbar */
.toolbar{position:absolute;left:0;top:137px;width:1200px;height:43px;background:var(--bar);border-bottom:1px solid #e2e2e2;font-size:11.5px}
.toolbar .abs{top:16px}
.red-link{color:var(--link-red);text-decoration:underline}

/* pagination */
.pager{position:absolute;left:0;width:1200px;height:38px;font-size:11px}
.pager .abs{top:13px}
.page-num{width:18px;text-align:center}
.page-num.current{background:#111;color:#fff;top:9px!important;height:19px;line-height:19px}
.rows-select{width:46px;height:22px;top:8px!important;border:1px solid #ccc;background:#f0f0f0;border-radius:3px;font-size:12px;line-height:20px;padding-left:10px}
.rows-select .spin{position:absolute;right:0;top:0;width:13px;height:20px;background:#555;border-radius:0 2px 2px 0}
.pager .label{font-size:12px;color:var(--navy);top:12px}
.shade{height:14px;top:22px!important;background:radial-gradient(ellipse at center,rgba(0,0,0,.12),rgba(0,0,0,0) 70%)}

/* table */
.data-table{position:absolute;left:0;top:232px;width:1200px;border-collapse:collapse;table-layout:fixed;font-size:12px}
.data-table th{height:40px;font-weight:400;color:#222;border-right:1px solid var(--rule);border-bottom:1px solid #bbb;text-align:center}
.data-table th:last-child,.data-table td:last-child{border-right:none}
.data-table td{height:32.6px;text-align:center;border-right:1px solid var(--rule);border-bottom:1px solid #c9c9c9;background:linear-gradient(#fdfdfd,#e7e7e7);color:#444;white-space:nowrap;overflow:hidden}
.data-table .name-last{text-align:left;padding-left:17px}
.data-table .name-first{text-align:left;padding-left:20px}
</style>
</head>
<body>

<header class="site-header">
  <div class="abs brand">
    <span class="brand-mark"></span>
    <span class="brand-name">PLUME-Finder</span>
  </div>
  <div class="abs welcome">Welcome ,<span class="user">Jack</span></div>
  <svg class="abs account-icon" style="left:703px" width="20" height="20" viewBox="0 0 20 20" aria-hidden="true">
    <circle cx="10" cy="6" r="4" fill="none" stroke="#333" stroke-width="1.4"/>
    <path d="M2 19c0-5 3.5-7 8-7s8 2 8 7z" fill="none" stroke="#333" stroke-width="1.4"/>
  </svg>
  <svg class="abs account-icon" style="left:770px" width="18" height="18" viewBox="0 0 18 18" aria-hidden="true">
    <rect x="1.5" y="1.5" width="15" height="15" rx="3" fill="none" stroke="#333" stroke-width="1.4"/>
    <path d="M13 9H5M8 6 5 9l3 3" fill="none" stroke="#333" stroke-width="1.4"/>
  </svg>
  <div class="abs account">my profile | Log out</div>
  <div class="abs search-field"></div>
  <div class="abs search-button">Search</div>
  <div class="abs search-options">Search options</div>
  <svg class="abs" style="left:1175px;top:65px" width="15" height="11" viewBox="0 0 16 12" aria-hidden="true"><path d="M0 6 6 0v4h10v4H6v4z" fill="#4a90d4"/></svg>
</header>

<nav class="main-nav">
  <div class="nav-tab" style="left:36px;width:104px">Instructions</div>
  <div class="nav-tab active" style="left:154px;width:116px">Student Data</div>
</nav>
<div class="nav-rule"></div>

<section class="toolbar">
  <span class="abs" style="left:32px">Showing 26 of 3.8 columns</span>
  <span class="abs red-link" style="left:198px">show / hide columns</span>
  <svg class="abs" style="left:309px;top:17px" width="15" height="11" viewBox="0 0 16 12" aria-hidden="true"><path d="M0 6 6 0v4h10v4H6v4z" fill="#4a90d4"/></svg>
  <span class="abs" style="left:349px">3 columns are <span class="red-link">filtered</span></span>
  <svg class="abs" style="left:1063px;top:10px" width="22" height="22" viewBox="0 0 22 22" aria-label="Print" role="img">
    <rect x="6" y="2" width="10" height="6" fill="#fff" stroke="#555"/>
    <rect x="1" y="8" width="20" height="9" rx="2" fill="#777"/>
    <rect x="5" y="14" width="12" height="6" fill="#fff" stroke="#555"/>
  </svg>
  <svg class="abs" style="left:1132px;top:10px" width="22" height="22" viewBox="0 0 22 22" aria-label="Download" role="img">
    <path d="M7 1h8v8h5l-9 9-9-9h5z" fill="var(--green)"/>
    <rect x="2" y="19" width="18" height="3" fill="var(--green)"/>
  </svg>
</section>

<div class="pager" style="top:184px">
  <span class="abs" style="left:27px">PAGE</span>
  <svg class="abs" style="left:63px;top:13px" width="15" height="12" viewBox="0 0 15 12" aria-hidden="true"><path d="M0 6 6 0v4h9v4H6v4z" fill="#4a90d4"/></svg>
  <span class="abs shade" style="left:110px;width:300px"></span>
  <span class="abs page-num" style="left:89px">1</span>
  <span class="abs page-num" style="left:112px">2</span>
  <span class="abs page-num" style="left:135px">3</span>
  <span class="abs page-num" style="left:158px">4</span>
  <span class="abs page-num" style="left:181px">5</span>
  <span class="abs page-num" style="left:203px">6</span>
  <span class="abs page-num current" style="left:226px">7</span>
  <span class="abs page-num" style="left:249px">8</span>
  <span class="abs page-num" style="left:271px">9</span>
  <span class="abs" style="left:298px">........</span>
  <span class="abs" style="left:333px">44</span>
  <span class="abs" style="left:358px">45</span>
  <span class="abs" style="left:383px">46</span>
  <span class="abs" style="left:408px">47</span>
  <svg class="abs" style="left:438px;top:13px" width="15" height="12" viewBox="0 0 15 12" aria-hidden="true"><path d="M15 6 9 0v4H0v4h9v4z" fill="#4a90d4"/></svg>
  <span class="abs label" style="left:495px">Show</span>
  <span class="abs rows-select" style="left:532px">10<span class="spin"></span></span>
  <span class="abs label" style="left:588px">rows per page</span>
</div>

<table class="data-table">
  <colgroup>
    <col style="width:50px"><col style="width:90px"><col style="width:80px"><col style="width:85px"><col style="width:99px"><col style="width:109px"><col style="width:129px"><col style="width:103px"><col style="width:75px"><col style="width:93px"><col style="width:103px"><col style="width:94px"><col style="width:90px">
  </colgroup>
  <thead>
    <tr><th>Date</th><th>Grade</th><th>ESC</th><th>CDC #</th><th>District</th><th>Campus</th><th>Last Name</th><th>First Name</th><th>MI</th><th>Student ID</th><th>Gender</th><th>DOB</th><th>Hisp</th></tr>
  </thead>
  <tbody>
    <tr><td>411</td><td>9</td><td>10</td><td>999999001</td><td>Example District</td><td>Example H S</td><td class="name-last">ABERNATHY</td><td class="name-first">NATALIA</td><td></td><td>512908476</td><td>F</td><td>4151997</td><td>1</td></tr>
    <tr><td>411</td><td>9</td><td>10</td><td>999999001</td><td>Example District</td><td>Example H S</td><td class="name-last">ACKERLY</td><td class="name-first">SHANE</td><td></td><td>512908476</td><td>M</td><td>4151997</td><td>1</td></tr>
    <tr><td>411</td><td>9</td><td>10</td><td>999999001</td><td>Example District</td><td>Example H S</td><td class="name-last">ADAIR</td><td class="name-first">EDWIN</td><td>I</td><td>512908476</td><td>M</td><td>4151997</td><td>1</td></tr>
    <tr><td>411</td><td>9</td><td>10</td><td>999999001</td><td>Example District</td><td>Example H S</td><td class="name-last">ALDRIDGE</td><td class="name-first">DAHLIA</td><td>E</td><td>512908476</td><td>F</td><td>4151997</td><td>1</td></tr>
    <tr><td>411</td><td>9</td><td>10</td><td>999999001</td><td>Example District</td><td>Example H S</td><td class="name-last">ALBRIGHT</td><td class="name-first">SUSAN</td><td></td><td>512908476</td><td>F</td><td>4151997</td><td>1</td></tr>
    <tr><td>411</td><td>9</td><td>10</td><td>999999001</td><td>Example District</td><td>Example H S</td><td class="name-last">ALMSTEAD</td><td class="name-first">KHALIL</td><td>M</td><td>512908476</td><td>M</td><td>4151997</td><td>1</td></tr>
    <tr><td>411</td><td>9</td><td>10</td><td>999999001</td><td>Example District</td><td>Example H S</td><td class="name-last">ALVORD</td><td class="name-first">IVANA</td><td>B</td><td>512908476</td><td>F</td><td>4151997</td><td>1</td></tr>
    <tr><td>411</td><td>9</td><td>10</td><td>999999001</td><td>Example District</td><td>Example H S</td><td class="name-last">ALVERSON</td><td class="name-first">RONALD</td><td>W</td><td>512908476</td><td>M</td><td>4151997</td><td>1</td></tr>
    <tr><td>411</td><td>9</td><td>10</td><td>999999001</td><td>Example District</td><td>Example H S</td><td class="name-last">ALWARD</td><td class="name-first">RODRIGO</td><td>J</td><td>512908476</td><td>M</td><td>4151997</td><td>1</td></tr>
  </tbody>
</table>

<div class="pager" style="top:562px">
  <span class="abs" style="left:27px">PAGE</span>
  <svg class="abs" style="left:63px;top:13px" width="15" height="12" viewBox="0 0 15 12" aria-hidden="true"><path d="M0 6 6 0v4h9v4H6v4z" fill="#4a90d4"/></svg>
  <span class="abs shade" style="left:110px;width:300px"></span>
  <span class="abs page-num" style="left:89px">1</span>
  <span class="abs page-num" style="left:112px">2</span>
  <span class="abs page-num" style="left:135px">3</span>
  <span class="abs page-num" style="left:158px">4</span>
  <span class="abs page-num" style="left:181px">5</span>
  <span class="abs page-num" style="left:203px">6</span>
  <span class="abs page-num current" style="left:226px">7</span>
  <span class="abs page-num" style="left:249px">8</span>
  <span class="abs page-num" style="left:271px">9</span>
  <span class="abs" style="left:298px">........</span>
  <span class="abs" style="left:333px">44</span>
  <span class="abs" style="left:358px">45</span>
  <span class="abs" style="left:383px">46</span>
  <span class="abs" style="left:408px">47</span>
  <svg class="abs" style="left:438px;top:13px" width="15" height="12" viewBox="0 0 15 12" aria-hidden="true"><path d="M15 6 9 0v4H0v4h9v4z" fill="#4a90d4"/></svg>
  <span class="abs label" style="left:495px">Show</span>
  <span class="abs rows-select" style="left:532px">10<span class="spin"></span></span>
  <span class="abs label" style="left:588px">rows per page</span>
</div>

</body>
</html>
```